Plate Parade! Digital Order Web App

This is a web app on mobile phone, for consumers to order food inside a restaurant using their phones. we have done up the flow but we need to revamp UI design. pls have a look at our current web on your mobile phone:
https://demo.pesanly.app/o/KWLM/274615

CURRENT DESIGN.
1. food category on left side, always shown. menu items in list view with image.
2. when we click on an item, there is popup page, to select modifiers, or quantity.
3. order review page(cart page) is quite messy now, need a complete new look.
4 payment page(no need to design, handle by Paxtel)
5. order confirmation page. success or error return

DESIGN requirements:
please browse through and click to order with current page above. we have put in lots of thoughts and effort for current flow, the new design should base on this flow.
1. web app. no zoom in/out is allowed for users. responsive html to suit different mobile phone screen size. modern fonts.
2. PAGES needed:
home/welcome page,
well laid out menu items page,
single item page, with add on choice and modifier
cart page(to include recommended items, ordered item list, remove item total, changeable quantity,
confirmation page(success, fail)

DELIVERABLES - responsive html, fonts, images asset such as icons, animation, button images(suitable for commercial use without further third party loyalty fee)

Hi all if we have left a comment on ur design, please revise accordingly and we will conclude it soon!

Target Market(s)

young diners who order food on their mobile phone.

Industry/Entity Type

Restaurant

Coding

Coded - Design and coding required

Number of Pages Required

5+ page

Colors

Designer to choose colors to be used in the design.

Requirements
Must have
• - lively, appetising colors while making the page easy to read. easy on eyes.
• - consistency. fonts used.
Nice to have
• - 2 color schemes
• - html codes. we will top up if you can deliver coded html.
Should not have
• - should not have more than 3 colors
• - should not have more than 3 different fonts
• - should not use colors that are dull

```html
<!DOCTYPE html>
<html lang="en">
<head>
<meta charset="utf-8">
<title>Plate Parade! – Vegetable Menu</title>
<meta name="viewport" content="width=device-width, initial-scale=1, maximum-scale=1, user-scalable=no">
<link rel="stylesheet" href="https://fonts.googleapis.com/css2?family=Noto+Sans+SC:wght@400;700&family=Roboto:wght@400;500;700&display=swap">
<style>
  :root {
    --charcoal: #1f1b19;
    --charcoal-bar: #2a2421;
    --page-bg: #f6f1ec;
    --card-bg: #ffffff;
    --accent: #ff6a2b;
    --accent-dark: #e5541a;
    --text-light: #ffffff;
    --text-dark: #1f1b19;
    --text-muted: #7a6f69;
    --lettuce-1: #c4e38f;
    --lettuce-2: #5f9a34;
    --oyster-1: #d9a55a;
    --oyster-2: #6a4220;
    --shiitake-1: #a3582a;
    --shiitake-2: #3a1e10;
  }
  * { box-sizing: border-box; margin: 0; padding: 0; }
  html, body { width: 100%; height: 100%; overflow: hidden; }
  body {
    display: flex;
    background: var(--page-bg);
    font-family: "Roboto", "Noto Sans SC", sans-serif;
    color: var(--text-dark);
  }

  /* Category sidebar */
  .sidebar {
    flex: 0 0 414px;
    height: 100%;
    background: var(--charcoal);
    padding: 34px 0 0 94px;
  }
  .brand {
    display: flex; align-items: center; gap: 12px;
    height: 56px;
    font-size: 44px; font-weight: 500; letter-spacing: 1px;
    color: var(--text-light);
  }
  .brand-dot {
    width: 12px; height: 12px; border-radius: 50%;
    background: var(--accent);
  }
  .category-list { list-style: none; margin-top: 14px; }
  .category-list li {
    height: 64.4px;
    line-height: 64.4px;
    font-size: 22px;
    color: var(--text-light);
  }
  .category-list li.is-active { color: var(--accent); font-weight: 500; }

  /* Content area */
  .content { flex: 1 1 auto; height: 100%; display: flex; flex-direction: column; min-width: 0; }
  .topbar {
    flex: 0 0 80px;
    display: flex; align-items: center; justify-content: space-between;
    padding: 0 46px 0 40px;
    background: var(--charcoal-bar);
  }
  .topbar-title { font-size: 25px; font-weight: 500; color: var(--text-light); }
  .cart-button { width: 48px; height: 40px; display: block; }

  .menu-grid {
    flex: 1 1 auto;
    overflow: hidden;
    padding: 36px 0 0 37px;
    display: grid;
    grid-template-columns: repeat(3, 224px);
    grid-auto-rows: 272px;
    column-gap: 18px; row-gap: 19px;
  }
  .dish-card {
    position: relative;
    background: var(--card-bg);
    border-radius: 4px;
    overflow: hidden;
    box-shadow: 0 2px 6px rgba(60, 30, 10, 0.12);
  }
  .dish-photo { height: 163px; }
  .photo-lettuce { background: linear-gradient(135deg, var(--lettuce-1), var(--lettuce-2)); }
  .photo-oyster { background: linear-gradient(135deg, var(--oyster-1), var(--oyster-2)); }
  .photo-shiitake { background: linear-gradient(135deg, var(--shiitake-1), var(--shiitake-2)); }
  .dish-info { padding: 12px 17px 0; }
  .dish-name {
    height: 24px; line-height: 24px;
    font-size: 15px; font-weight: 700; color: var(--text-dark);
    white-space: nowrap;
  }
  .dish-subname {
    height: 22px; line-height: 22px;
    font-size: 13px; color: var(--text-muted);
    white-space: nowrap;
  }
  .dish-card.shiitake .dish-name { font-size: 14px; }
  .dish-card.shiitake .dish-subname { font-weight: 500; }
  .dish-footer {
    display: flex; align-items: center; justify-content: space-between;
    margin-top: 10px;
  }
  .dish-price { font-size: 17px; font-weight: 700; color: var(--accent-dark); }
  .dish-card.shiitake .dish-price { font-size: 15px; }
  .add-to-cart {
    width: 82px; height: 22px;
    border: none; border-radius: 3px;
    background: var(--accent); color: var(--text-light);
    font-family: inherit; font-size: 8px; font-weight: 700; letter-spacing: 0.3px;
  }

  /* Phones */
  @media (max-width: 700px) {
    .sidebar { flex-basis: 104px; padding: 20px 0 0 14px; }
    .brand { font-size: 15px; height: 32px; gap: 6px; }
    .brand-dot { width: 8px; height: 8px; }
    .category-list li { height: 48px; line-height: 48px; font-size: 15px; }
    .topbar { flex-basis: 56px; padding: 0 14px; }
    .topbar-title { font-size: 19px; }
    .cart-button { width: 38px; height: 32px; }
    .menu-grid {
      padding: 14px;
      grid-template-columns: repeat(auto-fill, minmax(140px, 1fr));
      grid-auto-rows: auto; gap: 12px;
      overflow-y: auto;
    }
    .dish-photo { height: 110px; }
    .dish-info { padding: 8px 10px 10px; }
    .dish-name, .dish-card.shiitake .dish-name { font-size: 13px; white-space: normal; height: auto; }
    .dish-subname { font-size: 12px; white-space: normal; height: auto; }
    .dish-footer { flex-direction: column; align-items: flex-start; gap: 6px; }
    .add-to-cart { width: 100%; height: 28px; font-size: 10px; }
  }
</style>
</head>
<body>
  <aside class="sidebar">
    <div class="brand"><span class="brand-dot"></span>PESANLY</div>
    <ul class="category-list">
      <li class="is-active">Vegetable</li>
      <li>Meat</li>
      <li>Seafood</li>
      <li>Special</li>
      <li>Cold Dish</li>
      <li>Main</li>
      <li>Set</li>
      <li>Juice</li>
      <li>Drink</li>
      <li>Beer</li>
      <li>Alcohol</li>
      <li>Wine</li>
    </ul>
  </aside>

  <div class="content">
    <header class="topbar">
      <h1 class="topbar-title">Vegetable</h1>
      <svg class="cart-button" viewBox="0 0 48 40" role="img" aria-label="Cart, 2 items">
        <path d="M2 10 H8 L13 28 H30 L34 14 H10" fill="none" stroke="#ffffff" stroke-width="2" stroke-linejoin="round" stroke-linecap="round"/>
        <circle cx="15" cy="34" r="2.5" fill="#ffffff"/>
        <circle cx="28" cy="34" r="2.5" fill="#ffffff"/>
        <circle cx="36" cy="10" r="8" fill="#ff6a2b"/>
        <text x="36" y="13" text-anchor="middle" font-family="Roboto, sans-serif" font-size="9" font-weight="700" fill="#ffffff">02</text>
      </svg>
    </header>

    <main class="menu-grid">
      <article class="dish-card">
        <div class="dish-photo photo-lettuce" role="img" aria-label="Photo of grilled romaine lettuce"></div>
        <div class="dish-info">
          <h2 class="dish-name">Grilled Romaine Lettuce</h2>
          <p class="dish-subname">烤油麦菜</p>
          <div class="dish-footer"><p class="dish-price">S$1.30</p><button class="add-to-cart">ADD TO CART</button></div>
        </div>
      </article>
      <article class="dish-card">
        <div class="dish-photo photo-oyster" role="img" aria-label="Photo of grilled oyster mushroom skewers"></div>
        <div class="dish-info">
          <h2 class="dish-name">Grilled Oyster Mushroom</h2>
          <p class="dish-subname">烤鲜耗菇</p>
          <div class="dish-footer"><p class="dish-price">S$1.30</p><button class="add-to-cart">ADD TO CART</button></div>
        </div>
      </article>
      <article class="dish-card shiitake">
        <div class="dish-photo photo-shiitake" role="img" aria-label="Photo of grilled shiitake mushroom skewers"></div>
        <div class="dish-info">
          <h2 class="dish-name">烤香菇</h2>
          <p class="dish-subname">Grilled Shitake Mushroom</p>
          <div class="dish-footer"><p class="dish-price">S$1.30</p><button class="add-to-cart">ADD TO CART</button></div>
        </div>
      </article>

      <article class="dish-card">
        <div class="dish-photo photo-lettuce" role="img" aria-label="Photo of grilled romaine lettuce"></div>
        <div class="dish-info">
          <h2 class="dish-name">Grilled Romaine Lettuce</h2>
          <p class="dish-subname">烤油麦菜</p>
          <div class="dish-footer"><p class="dish-price">S$1.30</p><button class="add-to-cart">ADD TO CART</button></div>
        </div>
      </article>
      <article class="dish-card">
        <div class="dish-photo photo-oyster" role="img" aria-label="Photo of grilled oyster mushroom skewers"></div>
        <div class="dish-info">
          <h2 class="dish-name">Grilled Oyster Mushroom</h2>
          <p class="dish-subname">烤鲜耗菇</p>
          <div class="dish-footer"><p class="dish-price">S$1.30</p><button class="add-to-cart">ADD TO CART</button></div>
        </div>
      </article>
      <article class="dish-card shiitake">
        <div class="dish-photo photo-shiitake" role="img" aria-label="Photo of grilled shiitake mushroom skewers"></div>
        <div class="dish-info">
          <h2 class="dish-name">烤香菇</h2>
          <p class="dish-subname">Grilled Shitake Mushroom</p>
          <div class="dish-footer"><p class="dish-price">S$1.30</p><button class="add-to-cart">ADD TO CART</button></div>
        </div>
      </article>

      <article class="dish-card">
        <div class="dish-photo photo-lettuce" role="img" aria-label="Photo of grilled romaine lettuce"></div>
        <div class="dish-info">
          <h2 class="dish-name">Grilled Romaine Lettuce</h2>
          <p class="dish-subname">烤油麦菜</p>
          <div class="dish-footer"><p class="dish-price">S$1.30</p><button class="add-to-cart">ADD TO CART</button></div>
        </div>
      </article>
      <article class="dish-card">
        <div class="dish-photo photo-oyster" role="img" aria-label="Photo of grilled oyster mushroom skewers"></div>
        <div class="dish-info">
          <h2 class="dish-name">Grilled Oyster Mushroom</h2>
          <p class="dish-subname">烤鲜耗菇</p>
          <div class="dish-footer"><p class="dish-price">S$1.30</p><button class="add-to-cart">ADD TO CART</button></div>
        </div>
      </article>
      <article class="dish-card shiitake">
        <div class="dish-photo photo-shiitake" role="img" aria-label="Photo of grilled shiitake mushroom skewers"></div>
        <div class="dish-info">
          <h2 class="dish-name">烤香菇</h2>
          <p class="dish-subname">Grilled Shitake Mushroom</p>
          <div class="dish-footer"><p class="dish-price">S$1.30</p><button class="add-to-cart">ADD TO CART</button></div>
        </div>
      </article>
    </main>
  </div>
</body>
</html>
```